Energy Drink label Vumbalo

Design a Label to be used on the packaging label/mock up for a energy drink. The name VUMBALO means Black Bull & Bull ( in the 11 languages in the target country we want to launch ). I would like a in your face energy drink label design. Please see uploaded files as reference . Something out of the box thinking. For 500ml tin can label.

Target Market(s)

Population of Africa

Industry/Entity Type

Energy Drink

Colors
EB3D1F
EC4F4E
F09395
F8D3D4
FCEDEE

Requirements
Must have
• Bold and attractive design ( Black , Red , Silver , White ) as MAIN color scheme, as attached files I uploaded
Nice to have
• option of a white background and also black ( matte / carbon fibre effect )

```html
<!DOCTYPE html>
<html lang="en">
<head>
<meta charset="utf-8">
<title>Vumbalo Energy Drink – Can Label</title>
<link rel="stylesheet" href="https://fonts.googleapis.com/css2?family=Big+Shoulders+Display:wght@500&family=Graduate&family=Pathway+Gothic+One&family=Roboto+Mono:wght@700&display=swap">
<style>
  :root {
    --label-black: #151516;
    --label-charcoal: #2a2a2c;
    --bull-red: #c3202b;
    --bright-red: #ec4f4e;
    --deep-red: #5a0b10;
    --oval-red: #8e141c;
    --silver: #d9dcdf;
    --silver-dark: #8d9195;
    --ink: #1c1c1c;
    --white: #ffffff;
  }
  * { margin: 0; padding: 0; box-sizing: border-box; }
  html, body {
    width: 1200px;
    height: 960px;
    overflow: hidden;
    background: var(--label-black);
  }
  .label {
    position: relative;
    width: 1200px;
    height: 960px;
    background: linear-gradient(120deg, var(--label-black) 0%, var(--label-charcoal) 55%, var(--label-black) 100%);
    overflow: hidden;
  }
  .label-graphics {
    position: absolute;
    inset: 0;
  }
  .mascot-area {
    position: absolute;
    left: 430px;
    top: 170px;
    width: 340px;
    height: 310px;
    border-radius: 40% 40% 46% 46% / 30% 30% 70% 70%;
    background: linear-gradient(90deg, var(--bull-red) 0%, var(--bull-red) 50%, var(--ink) 50%, var(--ink) 100%);
  }
  .flavour-tag {
    position: absolute;
    left: 460px;
    top: 500px;
    width: 280px;
    height: 50px;
    border-radius: 4px;
    background: linear-gradient(90deg, #9a9ea2 0%, #f4f5f6 35%, #c9ccd0 70%, #7d8185 100%);
    font-family: "Graduate", serif;
    font-size: 34px;
    line-height: 50px;
    letter-spacing: 3px;
    text-align: center;
    color: var(--ink);
  }
  .brand-name {
    position: absolute;
    left: 0;
    width: 1200px;
    top: 548px;
    font-family: "Big Shoulders Display", sans-serif;
    font-weight: 500;
    font-size: 180px;
    line-height: 180px;
    letter-spacing: 4px;
    text-align: center;
    color: var(--silver);
  }
  .product-type {
    position: absolute;
    left: 0;
    width: 1200px;
    top: 728px;
    font-family: "Pathway Gothic One", sans-serif;
    font-size: 78px;
    line-height: 80px;
    text-align: center;
    color: var(--white);
  }
  .volume {
    position: absolute;
    left: 0;
    width: 1200px;
    top: 852px;
    font-family: "Roboto Mono", monospace;
    font-weight: 700;
    font-size: 44px;
    letter-spacing: 4px;
    text-align: center;
    color: var(--white);
  }
</style>
</head>
<body>
<main class="label">
  <svg class="label-graphics" width="1200" height="960" viewBox="0 0 1200 960" aria-hidden="true">
    <defs>
      <radialGradient id="oval-fill" cx="50%" cy="40%" r="65%">
        <stop offset="0%" stop-color="#a51a22"/>
        <stop offset="100%" stop-color="#4a0a0e"/>
      </radialGradient>
      <linearGradient id="silver-rim" x1="0" y1="0" x2="1" y2="1">
        <stop offset="0%" stop-color="#6d7175"/>
        <stop offset="45%" stop-color="#f2f3f4"/>
        <stop offset="100%" stop-color="#8d9195"/>
      </linearGradient>
    </defs>

    <g class="red-sweep-lines" fill="none" stroke-width="3">
      <path d="M140 0 C 260 300, 260 650, 120 960" stroke="#c3202b"/>
      <path d="M170 0 C 300 320, 300 650, 160 960" stroke="#ec4f4e"/>
      <path d="M1060 0 C 940 300, 940 650, 1080 960" stroke="#c3202b"/>
      <path d="M1030 0 C 900 320, 900 650, 1040 960" stroke="#ec4f4e"/>
      <path d="M700 0 L 1200 520" stroke="#c3202b"/>
      <path d="M740 0 L 1200 470" stroke="#ec4f4e"/>
      <path d="M780 0 L 1200 420" stroke="#c3202b"/>
      <path d="M1200 560 L 860 960" stroke="#c3202b"/>
      <path d="M1200 610 L 910 960" stroke="#ec4f4e"/>
      <path d="M0 520 L 340 960" stroke="#c3202b"/>
      <path d="M0 470 L 380 960" stroke="#ec4f4e"/>
      <path d="M500 0 L 0 430" stroke="#c3202b"/>
    </g>

    <ellipse class="emblem-rim" cx="600" cy="440" rx="275" ry="385" fill="url(#silver-rim)"/>
    <ellipse class="emblem-oval" cx="596" cy="434" rx="262" ry="372" fill="url(#oval-fill)"/>

    <g class="silver-streaks" stroke="#c9ccd0" stroke-width="2" fill="none" opacity="0.8">
      <path d="M800 130 L 830 420"/>
      <path d="M815 150 L 845 430"/>
      <path d="M400 130 L 370 420"/>
      <path d="M385 150 L 355 430"/>
    </g>
  </svg>

  <div class="mascot-area" role="img" aria-label="Bull head mascot illustration, half red and half black"></div>

  <div class="flavour-tag">ORIGINAL</div>
  <h1 class="brand-name">VUMBALO</h1>
  <p class="product-type">energy drink</p>
  <p class="volume">500 ml</p>
</main>
</body>
</html>
```